Business Card for Professional Photographer

I'm looking for an eye catching modern clean design that compliments my logo/ website fonts & colours.
I specialise in architecture, corporate & commercial photography so I'm marketing to professional clients rather than portrait / wedding clients.

I would prefer to not have a solid black design.

My logo brand guide is as follows :

Main front font. : Reislust
Main font colour : #fff
Slogan front font : Ubuntu Bold
Monogram front font : Venti Medium
Container colour : #fff

I need print ready files in pdf .png & .eps formats.

Included in the files below are some screen grabs as reference to font & colours etc.

```html
<!DOCTYPE html>
<html lang="en">
<head>
<meta charset="utf-8">
<title>Northlight Studio – Business Card</title>
<link href="https://fonts.googleapis.com/css2?family=Lato:wght@400;700&family=Raleway:wght@300;400&display=swap" rel="stylesheet">
<style>
  :root {
    --page-bg: #2a2624;
    --card-dark: #1c1b20;
    --gold: #cfa64e;
    --white: #ffffff;
    --rule: #34333a;
    --gap: #ffffff;
    --band: #0b0b0c;
  }
  * { margin: 0; padding: 0; box-sizing: border-box; }
  html, body {
    width: 1200px; height: 844px; overflow: hidden;
    background: var(--page-bg);
    font-family: "Lato", Arial, sans-serif;
  }
  .card {
    position: absolute;
    width: 540px; height: 309px;
    top: 268px;
    overflow: hidden;
    box-shadow: 0 12px 30px rgba(0,0,0,.45);
  }
  /* Front */
  .card-front { left: 50px; background: var(--card-dark); color: var(--white); }
  .brand {
    position: absolute; top: 48px; left: 0; right: 0;
    display: flex; align-items: center; justify-content: center; gap: 14px;
  }
  .brand-dot { width: 40px; height: 40px; border: 2px solid var(--gold); border-radius: 50%; }
  .brand-text { display: flex; flex-direction: column; }
  .brand-name {
    font-family: "Raleway", Arial, sans-serif; font-weight: 300;
    font-size: 22px; letter-spacing: 3px; color: var(--gold);
  }
  .brand-tagline {
    font-family: "Raleway", Arial, sans-serif; font-weight: 400;
    font-size: 8px; letter-spacing: 1.5px; color: var(--gold); margin-top: 3px;
  }
  .rule { position: absolute; left: 28px; right: 28px; height: 1px; background: var(--rule); }
  .rule-top { top: 150px; }
  .rule-mid { top: 248px; }
  .contact { position: absolute; left: 28px; top: 170px; }
  .person-name { font-weight: 700; font-size: 19px; color: var(--gold); letter-spacing: .5px; }
  .person-title { font-size: 14px; margin-top: 1px; }
  .address { position: absolute; left: 28px; top: 222px; font-size: 14px; }
  .lines { position: absolute; left: 28px; top: 262px; font-size: 13.5px; white-space: nowrap; }
  .label, .web { color: var(--gold); font-weight: 700; }
  .web { font-weight: 400; }

  /* Back */
  .card-back { left: 610px; background: var(--gap); }
  .tile { position: absolute; }
  .tile-car { left: 0; top: 0; width: 80px; height: 160px; background: linear-gradient(160deg,#a8916a,#5d5347); }
  .tile-garden { left: 86px; top: 0; width: 94px; height: 160px; background: linear-gradient(170deg,#3f6a33,#b96f6a 70%,#d9a08d); }
  .tile-building { left: 186px; top: 0; width: 354px; height: 110px; background: linear-gradient(180deg,#3f78c6,#a5bfdc 60%,#d8d9dc); }
  .tile-water { left: 0; top: 166px; width: 80px; height: 143px; background: linear-gradient(200deg,#3f6fb0,#0d2244); }
  .tile-bedroom { left: 86px; top: 166px; width: 200px; height: 72px; background: linear-gradient(120deg,#d9c6a8,#f0ebe3); }
  .tile-bath { left: 86px; top: 244px; width: 200px; height: 65px; background: linear-gradient(120deg,#f2f1ef,#e6c4cf); }
  .tile-clock { left: 292px; top: 184px; width: 100px; height: 125px; background: radial-gradient(circle at 55% 55%,#2c62c4,#8eb0e2 45%,#f1f1f1 70%); }
  .tile-interior { left: 398px; top: 184px; width: 142px; height: 125px; background: linear-gradient(140deg,#e3d6c3,#f4efe7 55%,#c9a886); }
  .band {
    position: absolute; left: 186px; top: 116px; width: 354px; height: 62px;
    background: var(--band);
    display: flex; align-items: center; justify-content: center; gap: 12px;
  }
  .band .brand-dot { width: 30px; height: 30px; }
  .band .brand-name { font-size: 17px; color: var(--white); }
  .band .brand-tagline { font-size: 6.5px; color: var(--white); }
</style>
</head>
<body>
  <section class="card card-front">
    <div class="brand">
      <span class="brand-dot"></span>
      <div class="brand-text">
        <span class="brand-name">NORTHLIGHT STUDIO</span>
        <span class="brand-tagline">Architecture Corporate Commercial</span>
      </div>
    </div>
    <div class="rule rule-top"></div>
    <div class="contact">
      <div class="person-name">DANIEL HART</div>
      <div class="person-title">Managing Director</div>
    </div>
    <div class="address">18, Harbour Road, Westfield, 20418</div>
    <div class="rule rule-mid"></div>
    <div class="lines">
      <span class="label">P:</span> 044-987 654 321 | <span class="label">E:</span>hello@northlight.com | <span class="web">www.northlightstudio.com</span>
    </div>
  </section>

  <section class="card card-back">
    <div class="tile tile-car" role="img" aria-label="Photo of classic car chassis in a garage"></div>
    <div class="tile tile-garden" role="img" aria-label="Photo of a person with a parasol in a garden"></div>
    <div class="tile tile-building" role="img" aria-label="Photo of modern white building under blue sky"></div>
    <div class="band">
      <span class="brand-dot"></span>
      <div class="brand-text">
        <span class="brand-name">NORTHLIGHT STUDIO</span>
        <span class="brand-tagline">Architecture Corporate Commercial</span>
      </div>
    </div>
    <div class="tile tile-water" role="img" aria-label="Photo of deep blue rippling water"></div>
    <div class="tile tile-bedroom" role="img" aria-label="Photo of a bright hotel bedroom"></div>
    <div class="tile tile-bath" role="img" aria-label="Photo of a white bathroom interior"></div>
    <div class="tile tile-clock" role="img" aria-label="Product photo of a blue-faced watch"></div>
    <div class="tile tile-interior" role="img" aria-label="Photo of a living room with a mirror"></div>
  </section>
</body>
</html>
```